Creative website for a boutique software house*

We are looking for someone who will design a creative website for a software house which will correspond to our core values.
We are a client oriented, quality focused and problem solving aimed people who love challenging tasks.
We want our clients to feel safe and taken care of during working with us, we combine software knowledge with business experience in different fields. We have a holistic approach to every project treating it as our own and putting our whole hearts into our work and relations with clients.
We value transparency and trust.
We still don’t have the copywriter to write texts for us, if you’ll have any questions we are here to answer

Target Market(s)

Startups

Number of Pages Required

4 page

Requirements
Must have
• Sections:
who we are
what we do (offer)
why the client should chose us
our core values

```html
<!DOCTYPE html>
<html lang="en">
<head>
<meta charset="utf-8">
<title>Korvel — Boutique Software House</title>
<link href="https://fonts.googleapis.com/css2?family=Roboto:wght@400;500;700&family=Raleway:wght@300;400;500&display=swap" rel="stylesheet">
<style>
:root{
  --gold:#f7cc00;
  --gold-deep:#e9b800;
  --brown:#7a5524;
  --brown-dark:#5a3d18;
  --ink:#222222;
  --text:#6f6f6f;
  --nav:#333333;
  --accent:#c8873a;
  --night:#141210;
  --footer:#616161;
  --white:#ffffff;
}
*{box-sizing:border-box;margin:0;padding:0}
html,body{width:1200px;height:3755px;overflow:hidden;background:var(--white)}
body{position:relative;font-family:"Raleway",sans-serif;color:var(--text)}
.abs{position:absolute}
.heading{font-family:"Roboto",sans-serif;font-weight:700;color:var(--ink);letter-spacing:.3px}
.btn{position:absolute;display:flex;align-items:center;justify-content:center;font-family:"Roboto",sans-serif;font-weight:500;font-size:15px;text-transform:uppercase;color:var(--ink)}
.btn-solid{background:var(--gold);box-shadow:0 3px 8px rgba(0,0,0,.18);border-radius:2px}
.btn-outline{border:1.5px solid var(--gold);color:var(--white);border-radius:2px}
/* header */
.site-header{position:absolute;left:0;top:0;width:1200px;height:90px;background:var(--white)}
.brand{position:absolute;left:114px;top:22px;display:flex;align-items:center;gap:10px;font-family:"Roboto",sans-serif;font-weight:400;font-size:30px;color:var(--brown)}
.brand-dot{width:26px;height:26px;border-radius:50%;background:var(--brown)}
.main-nav{position:absolute;left:437px;top:39px;display:flex;gap:31px;font-family:"Roboto",sans-serif;font-size:14px;color:var(--nav)}
.main-nav .active{color:var(--accent)}
/* hero */
.hero{position:absolute;left:0;top:90px;width:1200px;height:697px;background:linear-gradient(115deg,#4a3a2b 0%,#7b6a58 35%,#b9a996 60%,#6d5a46 100%)}
.hero-panel{position:absolute;left:0;top:251px;width:641px;height:215px;background:rgba(40,30,20,.55)}
.hero-title{left:110px;top:352px;font-size:52px;color:var(--white);font-weight:500}
.hero-copy{left:111px;top:416px;width:520px;font-size:16px;line-height:26px;color:var(--white)}
.scroll-label{left:583px;top:594px;font-size:12px;font-style:italic;color:var(--white);font-family:"Roboto",sans-serif}
/* who */
.who-title{left:112px;top:830px;font-size:41px}
.who-sub{left:113px;top:890px;font-size:24px;font-style:italic;color:var(--ink);font-family:"Roboto",sans-serif;font-weight:400}
.body-copy{font-size:15.5px;line-height:34.3px;text-align:justify;font-weight:400}
/* offer */
.offer-title{left:0;width:1200px;top:1480px;text-align:center;color:var(--white);font-size:41px}
.offer-card{position:absolute;top:1548px;height:275px;background:var(--white);border-radius:5px;overflow:hidden}
.offer-card .photo{height:213px}
.offer-card .label{height:62px;display:flex;align-items:center;justify-content:center;font-family:"Roboto",sans-serif;font-weight:500;font-size:15px;color:var(--ink)}
.offer-hover{position:absolute;left:0;top:0;width:100%;height:213px;background:rgba(122,85,36,.93);color:var(--white);text-align:center;padding:30px 30px 0;font-size:15.5px;line-height:31px}
.offer-hover span{color:var(--gold);text-decoration:underline;font-family:"Roboto",sans-serif;font-weight:500;font-size:14px}
/* core values */
.values-title{left:0;width:1200px;top:2020px;text-align:center;color:var(--gold);font-size:41px}
.values-copy{left:150px;width:900px;top:2078px;text-align:center;color:var(--white);font-size:15.5px;line-height:34.3px}
/* why */
.why-title{left:564px;top:2422px;font-size:41px}
/* blogs */
.blogs-title{left:0;width:1200px;top:2920px;text-align:center;font-size:41px}
.blog-card{position:absolute;top:2992px;width:320px;height:452px;border:1px solid #e2e2e2;background:var(--white)}
.blog-card .photo{position:absolute;left:8px;top:6px;width:302px;height:216px}
.blog-card h3{position:absolute;left:15px;top:240px;font-family:"Roboto",sans-serif;font-weight:500;font-size:15px;color:var(--ink)}
.blog-date{position:absolute;left:15px;top:272px;display:flex;align-items:center;gap:14px;font-size:15px}
.blog-card p{position:absolute;left:15px;top:305px;width:290px;font-size:14px;line-height:25px;text-align:justify}
.blog-card .btn{left:13px;top:394px;width:126px;height:38px;border-radius:19px;background:var(--gold);font-size:15px}
.share{position:absolute;top:403px;width:24px;height:22px;border:1px solid #cfcfcf}
/* footer */
.site-footer{position:absolute;left:0;top:3547px;width:1200px;height:208px;background:var(--footer);color:var(--white)}
.footer-nav{position:absolute;left:0;width:1200px;top:50px;display:flex;justify-content:center;gap:37px;font-size:15px}
.socials{position:absolute;left:0;width:1200px;top:89px;display:flex;justify-content:center;gap:23px}
.socials span{width:33px;height:33px;border:2px solid var(--white);border-radius:50%}
.copyright{position:absolute;left:0;width:1200px;top:142px;text-align:center;font-size:15px}
</style>
</head>
<body>

<header class="site-header">
  <div class="brand"><span class="brand-dot"></span>korvel</div>
  <nav class="main-nav">
    <span class="active">HOME</span><span>WHO WE ARE</span><span>WHAT WE DO</span><span>WHY CHOOSE</span><span>CORE VALUES</span><span>CONTACT</span>
  </nav>
</header>

<section class="hero" role="img" aria-label="Team of three colleagues reviewing work on a laptop in an office"></section>
<div class="hero-panel"></div>
<h1 class="abs heading hero-title">WELCOME TO KORVEL</h1>
<p class="abs hero-copy">We are a client oriented, quality focused and problem solvingaimed people who love challenging tasks.</p>
<div class="btn btn-outline" style="left:112px;top:477px;width:155px;height:52px">Get Started</div>
<span class="abs scroll-label">Scroll</span>
<svg class="abs" style="left:0;top:610px" width="1200" width="1200" height="180" viewBox="0 0 1200 180">
  <line x1="600" y1="15" x2="600" y2="104" stroke="#f7cc00" stroke-width="1.5"/>
  <circle cx="600" cy="15" r="10" fill="none" stroke="#f7cc00" stroke-width="2"/>
  <circle cx="600" cy="15" r="5" fill="#f7cc00"/>
  <path d="M0,167 Q600,-50 1200,167 L1200,180 L0,180 Z" fill="#7a5524"/>
  <path d="M0,182 Q600,-36 1200,182 L1200,182 L0,182 Z" fill="#ffffff"/>
</svg>

<section>
  <h2 class="abs heading who-title">WHO WE ARE</h2>
  <p class="abs who-sub">The Company</p>
  <p class="abs body-copy" style="left:114px;top:935px;width:510px">We are a boutique software house (focused on the client, bestquality of the service, lots of attention to the client and theirproduct, customized approach etc)We are a client oriented, quality focused and problem solvingaimed people who love challenging tasks.We want our clients to feel safe and taken care of during workingwith us, we combine software knowledge with business experiencein different fields. We have a holistic approach to every projecttreating it as our own and putting our whole hearts into our workand relations with clients.</p>
  <div class="btn btn-solid" style="left:112px;top:1225px;width:153px;height:51px">Read More</div>
  <svg class="abs" style="left:660px;top:852px" width="420" height="412" viewBox="0 0 420 412">
    <defs><linearGradient id="labTone" x1="0" y1="0" x2="1" y2="1"><stop offset="0" stop-color="#1c4d86"/><stop offset=".55" stop-color="#3a7fc0"/><stop offset="1" stop-color="#c9d9e6"/></linearGradient></defs>
    <circle cx="212" cy="205" r="201" fill="none" stroke="#f7cc00" stroke-width="5" stroke-dasharray="0 150 470 700"/>
    <circle cx="208" cy="205" r="199" fill="url(#labTone)" role="img" aria-label="Engineer working at monitors in a data lab"/>
  </svg>
</section>

<section>
  <div class="abs" style="left:0;top:1327px;width:1200px;height:590px;background:linear-gradient(180deg,#1e1a16,#100e0c)" role="img" aria-label="Dark office team background"></div>
  <svg class="abs" style="left:0;top:1320px" width="1200" height="90" viewBox="0 0 1200 90"><path d="M0,0 L1200,0 L1200,87 Q600,-65 0,87 Z" fill="#ffffff"/></svg>
  <h2 class="abs heading offer-title">WHAT CAN WE OFFER</h2>
  <div class="offer-card" style="left:111px;width:316px"><div class="photo" role="img" aria-label="Startup team meeting around a table" style="background:linear-gradient(135deg,#d8d4cc,#8d7a66)"></div><div class="label">EARLY STARTUPS</div></div>
  <div class="offer-card" style="left:436px;width:316px"><div class="photo" role="img" aria-label="Corporate office team" style="background:linear-gradient(135deg,#6e5a46,#3d3125)"></div><div class="offer-hover">The problem that most of the companies have right now with this kind of service is that you cannot really communicate<br><span>READ MORE ➜</span></div><div class="label">CORPORATIONS</div></div>
  <div class="offer-card" style="left:763px;width:316px"><div class="photo" role="img" aria-label="Open plan office with people at desks" style="background:linear-gradient(135deg,#e6e3de,#6a6560)"></div><div class="label">LATE STAGE STARTUPS</div></div>
</section>

<section>
  <div class="abs" style="left:0;top:1903px;width:1200px;height:425px;background:linear-gradient(180deg,#7d5826,#6f4d20)" role="img" aria-label="Warm brown office backdrop"></div>
  <svg class="abs" style="left:0;top:1890px" width="1200" height="95" viewBox="0 0 1200 95">
    <path d="M0,0 L1200,0 L1200,13 Q600,160 0,13 Z" fill="#121010"/>
    <path d="M0,13 Q600,160 1200,13" fill="none" stroke="#f7cc00" stroke-width="4"/>
  </svg>
  <h2 class="abs heading values-title">OUR CORE VALUES</h2>
  <p class="abs values-copy">Nemo enim ipsam voluptatem quia voluptas sit aspernatur aut odit aut fugit, sed quia consequuntur magni dolores eos qui ratione voluptatem sequi nesciunt. Neque porro quisquam est, qui dolorem ipsum quia dolor sit amet, consectetur, adipisci velit, sed quia non numquam eius modi tempora incidunt ut labore et dolore magnam aliquam quaerat voluptatem qui dolorem ipsum quia dolor sit amet, consectetur, adipisci</p>
  <div class="btn btn-outline" style="left:521px;top:2228px;width:154px;height:51px">Get Started</div>
</section>

<section>
  <svg class="abs" style="left:110px;top:2447px" width="420" height="412" viewBox="0 0 420 412">
    <defs><linearGradient id="pairTone" x1="0" y1="0" x2="1" y2="1"><stop offset="0" stop-color="#cfc9c2"/><stop offset=".5" stop-color="#efece8"/><stop offset="1" stop-color="#a89c90"/></linearGradient></defs>
    <circle cx="210" cy="204" r="201" fill="none" stroke="#f7cc00" stroke-width="5" stroke-dasharray="0 150 470 700"/>
    <circle cx="205" cy="204" r="199" fill="url(#pairTone)" role="img" aria-label="Two smiling colleagues at a laptop"/>
  </svg>
  <h2 class="abs heading why-title">WHY CHOOSE US</h2>
  <p class="abs body-copy" style="left:566px;top:2485px;width:510px">Nemo enim ipsam voluptatem quia voluptas sit aspernatur aut odit aut fugit, sed quia consequuntur magni dolores eos qui ratione voluptatem sequi nesciunt. Neque porro quisquam est, qui dolorem ipsum quia dolor sit amet, consectetur, adipisci velit, sed quia non numquam eius modi tempora incidunt ut labore et dolore magnam aliquam quaerat voluptatemNemo enim ipsam voluptatem quia voluptas sit aspernatur aut odit aut fugit, sed quia consequuntur magni dolores eos qui ratione voluptatem sequi nesciunt.</p>
  <div class="btn btn-solid" style="left:564px;top:2785px;width:153px;height:51px">Read More</div>
</section>

<section>
  <h2 class="abs heading blogs-title">LATEST BLOGS</h2>
  <article class="blog-card" style="left:111px">
    <div class="photo" role="img" aria-label="Colleagues discussing work at a computer" style="background:linear-gradient(135deg,#cfd3d6,#4c4a48)"></div>
    <h3>NEMO ENIM IPSAM VOLUPTATEM</h3>
    <div class="blog-date"><svg width="18" height="18" viewBox="0 0 18 18"><rect x="1" y="3" width="16" height="14" fill="none" stroke="#999"/><line x1="1" y1="7" x2="17" y2="7" stroke="#999"/></svg>March 13, 2020</div>
    <p>Nemo enim ipsam voluptatem quia voluptas sit aspernatur aut odit aut fugit, sed quia consequuntur</p>
    <div class="btn">Read More</div>
    <span class="share" style="left:199px"></span><span class="share" style="left:233px"></span><span class="share" style="left:267px"></span>
  </article>
  <article class="blog-card" style="left:434px">
    <div class="photo" role="img" aria-label="Two colleagues smiling over a tablet" style="background:linear-gradient(135deg,#9a9c9d,#3a3836)"></div>
    <h3>NEMO ENIM IPSAM VOLUPTATEM</h3>
    <div class="blog-date"><svg width="18" height="18" viewBox="0 0 18 18"><rect x="1" y="3" width="16" height="14" fill="none" stroke="#999"/><line x1="1" y1="7" x2="17" y2="7" stroke="#999"/></svg>March 13, 2020</div>
    <p>Nemo enim ipsam voluptatem quia voluptas sit aspernatur aut odit aut fugit, sed quia consequuntur</p>
    <div class="btn">Read More</div>
    <span class="share" style="left:199px"></span><span class="share" style="left:233px"></span><span class="share" style="left:267px"></span>
  </article>
  <article class="blog-card" style="left:758px">
    <div class="photo" role="img" aria-label="Team gathered around computers in an office" style="background:linear-gradient(135deg,#c4c8cc,#505256)"></div>
    <h3>NEMO ENIM IPSAM VOLUPTATEM</h3>
    <div class="blog-date"><svg width="18" height="18" viewBox="0 0 18 18"><rect x="1" y="3" width="16" height="14" fill="none" stroke="#999"/><line x1="1" y1="7" x2="17" y2="7" stroke="#999"/></svg>March 13, 2020</div>
    <p>Nemo enim ipsam voluptatem quia voluptas sit aspernatur aut odit aut fugit, sed quia consequuntur</p>
    <div class="btn">Read More</div>
    <span class="share" style="left:199px"></span><span class="share" style="left:233px"></span><span class="share" style="left:267px"></span>
  </article>
</section>

<footer class="site-footer">
  <nav class="footer-nav"><span>Home</span><span>Who We Are</span><span>What We Do</span><span>Why Choose</span><span>Core Values</span><span>Contact</span></nav>
  <div class="socials"><span></span><span></span><span></span><span></span></div>
  <p class="copyright">© 2020 All Rights Reserved</p>
</footer>

</body>
</html>
```